Wine label and name. Looking for a new wine label with catchy name for a cab blend

I'm looking for a wine label design and name for a new wine I'm blending in Sonoma County. I have a B&B there named Maison by the Orchard which I would like to tie in somehow, but use a unique, fun name. The wine will be a Cabernet blend. You can check out my website at www.hillcrestlodgingretreatvalleyside.com. Thanks, Marlo

Target Market(s)

Upscale red wine drinkers

Industry/Entity Type

Vineyard

Font styles to use
Script

Requirements
Must have
• Must have a design that incorporates the beauty of Sonoma County, the B&B and a catchy name.
Nice to have
• Humor and sexy. Fun and whimsical. Playful.

```html
<!DOCTYPE html>
<html lang="en">
<head>
<meta charset="utf-8">
<title>Velvet Tide – Cabernet Blend Label</title>
<link rel="stylesheet" href="https://fonts.googleapis.com/css2?family=Crimson+Text:wght@700&family=Poiret+One&family=Kaushan+Script&family=Fira+Sans:wght@500&family=Roboto+Condensed:wght@500&display=swap">
<style>
  :root {
    --label-brown: #332c29;
    --ink-white: #ffffff;
    --sunset-orange: #c46a35;
    --sky-amber: #a9683a;
    --sea-gold: #d9a65e;
    --sand-light: #c79351;
    --sand-deep: #7f5a30;
  }
  html, body {
    margin: 0;
    padding: 0;
    overflow: hidden;
    background: var(--label-brown);
  }
  .label {
    position: relative;
    width: 686px;
    height: 1200px;
    background: var(--label-brown);
    color: var(--ink-white);
    overflow: hidden;
  }
  .label p, .label h1 {
    position: absolute;
    left: 0;
    width: 100%;
    margin: 0;
    text-align: center;
    color: var(--ink-white);
    white-space: nowrap;
  }
  .wine-name {
    top: 28px;
    font-family: "Kaushan Script", cursive;
    font-weight: 400;
    font-size: 104px;
    line-height: 150px;
  }
  .coastal-scene {
    position: absolute;
    top: 213px;
    left: 0;
    width: 686px;
    height: 642px;
    background: linear-gradient(180deg,
      var(--sunset-orange) 0%,
      var(--sky-amber) 9%,
      #8f6a48 14%,
      var(--sea-gold) 32%,
      var(--sand-light) 55%,
      #a8753d 78%,
      var(--sand-deep) 100%);
  }
  .varietal {
    top: 758px;
    font-family: "Crimson Text", serif;
    font-weight: 700;
    font-size: 74px;
    line-height: 90px;
  }
  .appellation {
    top: 884px;
    font-family: "Poiret One", sans-serif;
    font-size: 44px;
    line-height: 56px;
  }
  .region-vintage {
    top: 962px;
    font-family: "Kaushan Script", cursive;
    font-size: 76px;
    line-height: 100px;
    letter-spacing: 4px;
  }
  .producer-name {
    top: 1108px;
    font-family: "Fira Sans", sans-serif;
    font-weight: 500;
    font-size: 32px;
    line-height: 40px;
  }
  .producer-type {
    top: 1148px;
    font-family: "Roboto Condensed", sans-serif;
    font-weight: 500;
    font-size: 19px;
    line-height: 22px;
  }
</style>
</head>
<body>
  <main class="label">
    <h1 class="wine-name">Velvet Tide</h1>
    <div class="coastal-scene" role="img" aria-label="Photograph of a Sonoma coast beach at sunset with dark rocks on wet golden sand"></div>
    <p class="varietal">Cabernet blend</p>
    <p class="appellation">Alexander Valley</p>
    <p class="region-vintage">California 2015</p>
    <p class="producer-name">Maison by the Orchard</p>
    <p class="producer-type">Bed and Breakfast</p>
  </main>
</body>
</html>
```